Business card design needed

I need a business card for a new company based in Perth, Western Australia, called KT Power Pty Ltd.

I'm the sole proprietor, and have 25 years' experience in directorship, senior commercial/business development/strategy roles in the oil & gas industry with both supermajors and junior listed companies. I also have interests in renewable energy (and am co-founder and director of a separate renewable energy start-up company). KT Power will be the vehicle for me to contract my services, principally in the oil & gas industry (although this will include directorship services to the renewable energy company). These services will include general consultancy in my areas of expertise, and contracting to provide senior management/director services to start-up or junior oil and gas companies.

I'm looking for a design that communicates professionalism, dynamism, experience, strategic skills and growth.

My ConnectHub profile may also be useful context;

"I have a real passion for discovering new investment opportunities and turning them from talk into reality. Right now my focus is on oil, gas and energy ventures. I’m always on the look out for compelling new investment opportunities where I can bring my leadership and strategic insight to bear to make a real difference by delivering transformational results.

I spent 24 years with HX where I built up extensive international experience in oil, gas and energy and was a member of the company’s “fast track” development programme. As an entrepreneurial senior commercial leader, strategic thinker and tactical dealmaker I was responsible for numerous deals such as divestments, farm-ins, asset swaps, new acreage bids, unitizations, gas and LNG sales, creating billions of dollars of value for HX. These deals frequently broke new ground and/or required an innovative approach that delivered results in excess of what the business thought achievable. I have held senior executive and director roles covering Exploration & Production, Mergers & Acquisitions, Business Development, LNG Marketing, Joint Venture Management, Gas & Power and Corporate head office. International assignments included UK, Australia, Indonesia, Norway & Belgium.

I’m a member of the Guild of Global Fuel Brokers (GGFB) and the Southern Council of Board Members (SCBM).

Board experience comprises four directorships and two alternate directorships of Australian companies, and directorship of a Not for Profit organisation.

Specialties
Strategy, Business Development, Mergers & Acquisitions, Joint Venture Management, Negotiation, Gas & LNG Marketing."

Target Market(s)

Oil and gas or energy companies of all sizes from large listed companies to start-ups - also service providers to the industry.

Industry/Entity Type

Oil And Gas

Contact Information for Business Card

KT Power Pty Ltd
Daniel Hobart
27C Lorne Avenue,
Kelmsdale,
WA 6093

Tel +61 455 823 617
email hobartdk@vellimo.net.au

```html
<!DOCTYPE html>
<html lang="en">
<head>
<meta charset="utf-8">
<title>KT Power Pty Ltd – Business Card</title>
<link rel="stylesheet" href="https://fonts.googleapis.com/css2?family=Source+Sans+3:wght@400&family=Roboto+Condensed:wght@300;400&family=Orbitron:wght@700&display=swap">
<style>
  :root {
    --page: #ffffff;
    --card-border: #8a8a8a;
    --blue-deep: #0a4db3;
    --blue-mid: #1f74d6;
    --blue-light: #5fb2f5;
    --accent-blue: #1c8ce0;
    --name-grey: #5f6266;
    --title-grey: #a9a9a9;
    --band-light: #cfcfcf;
    --band-dark: #6c6c6c;
    --white: #ffffff;
  }
  * { margin: 0; padding: 0; box-sizing: border-box; }
  html, body {
    width: 1200px; height: 741px; overflow: hidden;
    background: var(--page);
  }
  .card {
    position: absolute; left: 70px; top: 84px;
    width: 1060px; height: 574px;
    background: var(--white);
    border: 1px solid var(--card-border);
    overflow: hidden;
  }
  .card__artwork {
    position: absolute; left: 0; top: 0;
    width: 1060px; height: 487px;
  }
  .services {
    position: absolute; left: 48px; top: 36px;
    list-style: none;
    font-family: "Source Sans 3", sans-serif;
    font-size: 27px; line-height: 40px;
    color: var(--white);
  }
  .company-name {
    position: absolute; left: 40px; top: 322px;
    width: 980px;
    font-family: "Orbitron", sans-serif;
    font-weight: 700;
    font-size: 50px; letter-spacing: 5px;
    line-height: 60px;
    color: var(--name-grey);
    text-align: center;
    white-space: nowrap;
  }
  .company-mark {
    position: absolute; left: 893px; top: 192px;
    width: 126px; height: 126px; border-radius: 50%;
    background: var(--blue-mid);
  }
  .person {
    position: absolute; right: 48px; top: 400px;
    font-family: "Roboto Condensed", sans-serif;
    font-size: 30px; line-height: 36px;
    white-space: nowrap;
  }
  .person__name { color: var(--accent-blue); }
  .person__role { color: var(--title-grey); }
  .contact-band {
    position: absolute; left: 0; bottom: 0;
    width: 100%; height: 87px;
    background: linear-gradient(90deg, var(--band-light), var(--band-dark));
    display: flex; align-items: center; justify-content: center;
    font-family: "Roboto Condensed", sans-serif;
    font-weight: 300;
    font-size: 27px;
    color: var(--white);
    white-space: nowrap;
  }
</style>
</head>
<body>
  <div class="card">
    <svg class="card__artwork" viewBox="0 0 1060 487" role="img" aria-label="Abstract blue energy illustration with glowing light flares and orbit rings">
      <defs>
        <radialGradient id="energyGlow" cx="470" cy="140" r="620" gradientUnits="userSpaceOnUse">
          <stop offset="0" stop-color="var(--blue-light)"/>
          <stop offset="0.45" stop-color="var(--blue-mid)"/>
          <stop offset="1" stop-color="var(--blue-deep)"/>
        </radialGradient>
      </defs>
      <path d="M0 0 H566 C640 80 675 200 658 281 C645 370 630 430 611 487 H0 Z" fill="url(#energyGlow)"/>
    </svg>

    <ul class="services">
      <li>Strategy</li>
      <li>Business Development</li>
      <li>Mergers &amp; Acquisitions</li>
      <li>Joint Venture Management</li>
      <li>Negotiation</li>
    </ul>

    <div class="company-mark" aria-hidden="true"></div>
    <h1 class="company-name">KT POWER PTY LTD.</h1>

    <p class="person">
      <span class="person__name">Daniel Hobart</span>
      <span class="person__role">Director</span>
    </p>

    <p class="contact-band">27C Lorne Avenue. Kelmsdale. WA 6093. +61 455 823 617. daniel.hobart@ktpower.com.au</p>
  </div>
</body>
</html>
```